Waste Oil Filter collection & disposal

Basically I need a 1 page website for the business called Brenmoor Waste Solutions.
We are a environmental service provider and we collect and dispose of waste oil filters to protect the environment from hazardous waste oil products.

This is the link to our current website: www.brenmoorwaste.co.nz

we want it to look fresh and better than our current website. we may potentially look at getting a new logo designed and are open to ideas/designs if you have any.

Industry/Entity Type

Business

Logo Text

Brenmoor Waste Solutions

Number of Pages Required

1 page

Requirements
Must have
• same colours as current website.
• description of what service we provide please refer to leaflet attached

```html
<!DOCTYPE html>
<html lang="en">
<head>
<meta charset="utf-8">
<title>Brenmoor Waste Solutions</title>
<link rel="stylesheet" href="https://fonts.googleapis.com/css2?family=Montserrat:wght@300;400;500;600;700&display=swap">
<style>
:root{
  --green:#6cbf45;
  --green-dark:#58a536;
  --blue:#2b3f98;
  --ink:#222;
  --dark:#252525;
  --footer:#2a2727;
  --footer-cell:#383434;
  --white:#fff;
}
*{box-sizing:border-box;margin:0;padding:0}
html,body{width:1200px;height:2866px;overflow:hidden}
body{font-family:"Montserrat",sans-serif;color:var(--ink);background:var(--white);position:relative}
section,header,footer{position:absolute;left:0;width:1200px}
h1,h2{font-weight:400}
.abs{position:absolute}

/* header */
.site-header{top:0;height:96px;background:var(--white)}
.brand{left:80px;top:22px;height:52px;display:flex;align-items:center;gap:14px}
.brand-dot{width:52px;height:52px;border-radius:50%;border:3px solid var(--green)}
.brand-name{font-weight:700;font-size:24px;color:var(--blue);letter-spacing:.3px;line-height:1}
.nav{left:546px;top:40px;display:flex;gap:22px;font-size:13px;color:#333}
.nav .active{color:var(--blue);border-bottom:1px solid var(--blue)}
.nav-phone{left:1000px;top:36px;font-size:17px;color:var(--green);font-weight:500;display:flex;align-items:center;gap:7px}

/* hero */
.hero{top:96px;height:481px}
.hero-photo{position:absolute;inset:0;background:linear-gradient(180deg,#6b6a66 0%,#4d4b47 45%,#2d2c2b 100%)}
.hero-text{position:absolute;top:200px;width:100%;text-align:center;color:var(--white);text-shadow:0 1px 3px rgba(0,0,0,.4)}
.hero-text h1{font-size:29px;letter-spacing:.3px}
.hero-text p{font-size:17px;margin-top:2px}
.hero-chevron{left:592px;top:420px}

/* quote */
.quote-band{top:577px;height:159px;background:var(--green)}
.quote-mark{left:152px;top:30px;font-size:120px;font-weight:700;color:var(--green-dark);line-height:1;font-family:Georgia,serif}
.quote-text{left:254px;top:60px;font-size:14px;line-height:1.5;color:#1d2a12;width:480px}
.quote-cite{left:968px;top:72px;font-size:12px;font-weight:600;color:#1d2a12}

/* features */
.features{top:736px;height:539px}
.features-photo{left:0;top:0;width:600px;height:539px;background:linear-gradient(160deg,#5b6a6c 0%,#3f4e52 50%,#2f3a3f 100%)}
.feature{left:662px;display:flex;gap:36px;width:440px}
.feature svg{flex:none}
.feature p{font-size:17px;line-height:1.33;color:#222;width:300px}
.btn-green{left:665px;top:426px;width:126px;height:33px;background:var(--green);color:var(--white);font-size:12px;display:flex;align-items:center;justify-content:center}

/* pricing */
.pricing{top:1275px;height:441px;background:var(--blue)}
.section-title-light{top:74px;width:100%;text-align:center;color:var(--white);font-size:29px}
.plan{top:148px;width:260px;text-align:center;color:var(--white)}
.plan-icon{width:100px;height:68px;margin:0 auto;background:var(--green);border-radius:8px}
.plan-name{font-size:17px;font-weight:300;margin-top:28px;color:#d7dcf0}
.plan-price{font-size:29px;margin-top:4px}
.plan-price.small{font-size:25px}
.btn-outline{left:520px;top:328px;width:160px;height:33px;border:1px solid var(--green);color:var(--green);font-size:12px;display:flex;align-items:center;justify-content:center}

/* process */
.process{top:1716px;height:382px}
.section-title{top:73px;width:100%;text-align:center;font-size:29px;color:var(--blue)}
.section-sub{top:115px;width:100%;text-align:center;font-size:13px;color:#333}
.step{top:174px;width:208px;height:126px;text-align:center}
.step.div{border-left:1px solid #e3e3e3}
.step-num{width:46px;height:46px;border-radius:50%;background:var(--green);color:var(--white);font-size:13px;font-weight:700;display:flex;align-items:center;justify-content:center;margin:24px auto 0}
.step-num.soft{background:#a9d98f}
.step-label{font-size:13px;font-weight:600;line-height:1.45;margin-top:6px;color:#222}

/* oil */
.oil{top:2098px;height:237px;background:radial-gradient(circle at 80% 40%,#3a3a3a,var(--dark) 60%);color:var(--white);text-align:center}
.oil h2{position:absolute;top:72px;width:100%;font-size:29px}
.oil p{position:absolute;top:118px;width:100%;font-size:17px;line-height:1.4}
.oil em{font-style:normal;color:var(--green)}

/* contact */
.contact{top:2335px;height:466px}
.contact-title{left:155px;top:82px;font-size:29px;color:var(--blue)}
.contact-lead{left:155px;top:122px;font-size:17px}
.contact-addr{left:155px;top:163px;font-size:12px;line-height:1.6}
.contact-phone{left:155px;top:210px;font-size:17px;font-weight:600;color:var(--green)}
.contact-mail{left:155px;top:238px;font-size:12px;color:var(--blue);text-decoration:underline}
.contact-hours{left:155px;top:275px;font-size:12px;line-height:1.6}
.contact-hours strong{font-size:14px;font-weight:500}
.btn-blue{left:157px;top:354px;width:158px;height:33px;background:var(--blue);color:var(--white);font-size:12px;display:flex;align-items:center;justify-content:center;gap:8px}
.map{left:535px;top:83px;width:508px;height:302px;background:linear-gradient(135deg,#ececec,#dcdcdc)}

/* footer */
.site-footer{top:2801px;height:65px;background:var(--footer)}
.copyright{left:155px;top:26px;font-size:11px;color:#bbb}
.foot-cell{top:0;width:104px;height:65px;background:var(--footer-cell);border-left:1px solid #2a2727;display:flex;align-items:center;justify-content:center}
</style>
</head>
<body>

<header class="site-header">
  <div class="abs brand">
    <div class="brand-dot"></div>
    <div class="brand-name">Brenmoor Waste Solutions</div>
  </div>
  <nav class="abs nav">
    <span class="active">What We Do</span><span>Why Us</span><span>Pricing</span><span>The Process</span><span>Contact Us</span>
  </nav>
  <div class="abs nav-phone">
    <svg width="16" height="16" viewBox="0 0 16 16"><circle cx="8" cy="8" r="7" fill="none" stroke="var(--green)" stroke-width="1.5"/><path d="M5.5 4.5l1.5 1.5-1 1.2a6 6 0 0 0 2.8 2.8l1.2-1 1.5 1.5-1 1.2c-2.5 0-6-3.5-6-6z" fill="var(--green)"/></svg>
    06 555 0142
  </div>
</header>

<section class="hero">
  <div class="hero-photo" role="img" aria-label="Pile of used oil and fuel filters"></div>
  <div class="hero-text">
    <h1>Specialize in the collection &amp; disposal</h1>
    <p>of oil / fuel filters, servicing the lower north island on a monthly cycle.</p>
  </div>
  <svg class="abs hero-chevron" width="16" height="10" viewBox="0 0 16 10"><path d="M2 2l6 6 6-6" fill="none" stroke="#fff" stroke-width="2"/></svg>
</section>

<section class="quote-band">
  <div class="abs quote-mark">“</div>
  <p class="abs quote-text">Each used oil filter has on average, more than quarter of a litre of used motor oil.</p>
  <div class="abs quote-cite">– CleanOil Trust</div>
</section>

<section class="features">
  <div class="abs features-photo" role="img" aria-label="Filter processing plant with conveyor and hoist"></div>
  <div class="abs feature" style="top:80px">
    <svg width="42" height="42" viewBox="0 0 42 42"><circle cx="21" cy="21" r="19" fill="none" stroke="var(--blue)" stroke-width="2"/><path d="M12 21l7 7 16-17" fill="none" stroke="var(--blue)" stroke-width="2.5"/></svg>
    <p>We are passionate about doing our bit in keeping NZ Clean and Green.</p>
  </div>
  <div class="abs feature" style="top:170px">
    <svg width="42" height="42" viewBox="0 0 42 42"><circle cx="21" cy="21" r="19" fill="none" stroke="var(--blue)" stroke-width="2"/><path d="M12 21l7 7 16-17" fill="none" stroke="var(--blue)" stroke-width="2.5"/></svg>
    <p>We offer a cost effective system for the collection and disposal of waste oil filters.</p>
  </div>
  <div class="abs feature" style="top:260px">
    <svg width="42" height="42" viewBox="0 0 42 42"><circle cx="21" cy="21" r="19" fill="none" stroke="var(--blue)" stroke-width="2"/><path d="M12 21l7 7 16-17" fill="none" stroke="var(--blue)" stroke-width="2.5"/></svg>
    <p>ECO friendly processes and minimise the contamination of landfills.</p>
  </div>
  <div class="abs feature" style="top:350px">
    <svg width="42" height="42" viewBox="0 0 42 42"><circle cx="21" cy="21" r="19" fill="none" stroke="var(--blue)" stroke-width="2"/><path d="M12 21l7 7 16-17" fill="none" stroke="var(--blue)" stroke-width="2.5"/></svg>
    <p>We keep your industry compliant</p>
  </div>
  <div class="abs btn-green">Contact Us</div>
</section>

<section class="pricing">
  <h2 class="abs section-title-light">Pricing Packages</h2>
  <div class="abs plan" style="left:166px">
    <div class="plan-icon" role="img" aria-label="Collection truck icon"></div>
    <div class="plan-name">Monthly Bin Collection</div>
    <div class="plan-price">$65.00</div>
  </div>
  <div class="abs plan" style="left:470px">
    <div class="plan-icon" role="img" aria-label="Recycling bins icon"></div>
    <div class="plan-name">Additional Bins</div>
    <div class="plan-price">$35.00</div>
  </div>
  <div class="abs plan" style="left:766px">
    <div class="plan-icon" role="img" aria-label="Account sign-up icon"></div>
    <div class="plan-name">Account Set Up Fee</div>
    <div class="plan-price small">$85.00</div>
  </div>
  <div class="abs btn-outline">Ready to Help You</div>
</section>

<section class="process">
  <h2 class="abs section-title">The Process</h2>
  <p class="abs section-sub">Filters are collected and transported back to the processing plant.</p>
  <div class="abs step" style="left:80px"><div class="step-num">01.</div><div class="step-label">Drained Oil<br>Filter</div></div>
  <div class="abs step div" style="left:288px"><div class="step-num soft">02.</div><div class="step-label">Sorted &amp; Drained<br>Again</div></div>
  <div class="abs step div" style="left:496px"><div class="step-num">03.</div><div class="step-label">Crushed into<br>Bricks</div></div>
  <div class="abs step div" style="left:704px"><div class="step-num">03.</div><div class="step-label">Drained a 3rd<br>Time</div></div>
  <div class="abs step div" style="left:912px"><div class="step-num">05.</div><div class="step-label">Ready for Metal<br>Recycling</div></div>
</section>

<section class="oil">
  <h2>What Happens to the Oil</h2>
  <p>All residual oil is <em>collected into our tank</em> and then recycled. Currently we are processing<br><em>over 2,000 litres</em> of oil a month.</p>
</section>

<section class="contact">
  <h2 class="abs contact-title">Ready to help you</h2>
  <p class="abs contact-lead">Contact us today!</p>
  <p class="abs contact-addr">Brenmoor Waste Solutions Ltd<br>Harbour Lane, Kerrow 4820, New Zealand</p>
  <p class="abs contact-phone">Call Us: 06 555 0142</p>
  <p class="abs contact-mail">help@brenmoorwaste.co.nz</p>
  <p class="abs contact-hours"><strong>Opening Hours</strong><br>Mon - Fri: &nbsp;7.30am - 5.00pm</p>
  <div class="abs btn-blue">
    <svg width="10" height="14" viewBox="0 0 10 14"><path d="M5 0a5 5 0 0 0-5 5c0 4 5 9 5 9s5-5 5-9a5 5 0 0 0-5-5z" fill="#fff"/><circle cx="5" cy="5" r="2" fill="var(--blue)"/></svg>
    Get Directions
  </div>
  <div class="abs map" role="img" aria-label="Street map showing the depot location"></div>
</section>

<footer class="site-footer">
  <p class="abs copyright">© 2017 Brenmoor Waste Solutions Ltd</p>
  <div class="abs foot-cell" style="left:887px"></div>
  <div class="abs foot-cell" style="left:992px"></div>
  <div class="abs foot-cell" style="left:1096px">
    <svg width="12" height="16" viewBox="0 0 12 16"><path d="M6 15V2M1 7l5-5 5 5" fill="none" stroke="#ddd" stroke-width="1.8"/></svg>
  </div>
</footer>

</body>
</html>
```